VidTrellis banner - Girl illustration, technology, green, blue, spring-like

I need help for vidtrellis art for my banner. There are strict channel art templates. I have no ideas at all but hope if you look at some of my videos you will learn a bit about me.

My channel:
https://www.vidtrellis.example/channel/QTZPfM2w8Lk3N7Hcdra5Ypx

My channel is on Unix, technology, information security, and some technical demonstration videos.

Channel templates can be found here
https://help.corvanthe.example/vidtrellis/answer/5816407?hl=en

Here is what I don't like:
- pictures of "hackers" - boys with hoodies on
- pictures of circuit boards

Can show my name "LP Thornbury" preferred, cursive is good, or blackboard type fun font

or "Lise-Paule Thornbury" is an option

vQuarn.ca is my company webpage, but we are not really using the logo or company name much so it does not need to feature
Updates

Oh, and I am Canadian and an outdoor lover :-) that means that silhouettes of maple leaves, and moose and other Canadian symbols would be something I like also...*AND* I recently caught my hair and now have bangs (fringe) so if you are making an image of me that is important. Also I have green eyes. - I will upload a photo. Added Thursday, November 24, 2016

Target Market(s)

My viewers are currently majority 25-35 year old males, but am trying to appeal to girls too.

Industry/Entity Type

Computer Security

Logo Text

LP Thornbury

Logo styles of interest
Pictorial/Combination Logo
Font styles to use
Sans Serif
Decorative
Script
Other font styles liked:
• Blackboard

Colors
33a6d7
33b8a4
00a990
3276b5
0255a3
6b449b
b7a5cd
fbee3e
faa54b

Requirements
Must have
• Must conform to the vidtrellis channel art template and look great on all devices: TV, computer, tablet and phone. 2560 x 1440 px and 4MB or smaller in JPEG or PNG format
• Channel templates can be found here
• https://help.corvanthe.example/vidtrellis/answer/5816407?hl=en
• On a TV display, the whole image is displayed as channel art. The aspect ratio is 16:9 (i.e. 2560 x 1440 px).
• Minimum width: 2048 X 1152 px. This is the "safe area," where text and logos are guaranteed not to be cut off when displayed on different devices.
• Maximum width: 2560 X 423 px. This means that the "safe area" is always visible; the areas to each side of the channel art are visible depending on the viewer’s browser size.
• File size: 4MB or smaller recommended.
• If you're not sure about the width and height of an image, download our Channel Art Templates to see how images show on different devices. You can use your computer's image editor or find one online to resize the images.
Nice to have
• I'm pretty open, but here is what I like:
• - colours blue, green, bright and spring like
• - unisex appeal
• - cool girl hackers are okay
• - I like birds, stylized doves are good, hummingbirds are a favorite
• - cartoon or anime girls may appeal to me. with dreadlocks or yarn-like hair are a bonus - if you do an illustration of me, I have green eyes and bangs (fringe)
• - design should be fun but elegant
Should not have
• Here is what I don't like:
• - pictures of "hackers" - boys with hoodies on
• - pictures of circuit boards

```html
<!DOCTYPE html>
<html lang="en">
<head>
<meta charset="utf-8">
<title>LP Thornbury — Channel Banner</title>
<link href="https://fonts.googleapis.com/css2?family=Mrs+Saint+Delafield&display=swap" rel="stylesheet">
<style>
  :root {
    --bg: #5f4899;
    --bg-deep: #553f8f;
    --tint: #7a66b3;
    --tint-soft: rgba(255, 255, 255, 0.12);
    --line-pink: rgba(196, 92, 170, 0.45);
    --white: #ffffff;
    --white-soft: rgba(255, 255, 255, 0.55);
    --white-faint: rgba(255, 255, 255, 0.22);
    --shadow: rgba(40, 20, 70, 0.75);
  }
  * { margin: 0; padding: 0; box-sizing: border-box; }
  html, body {
    width: 1200px;
    height: 328px;
    overflow: hidden;
    background: var(--bg);
  }
  .banner {
    position: relative;
    width: 1200px;
    height: 328px;
    overflow: hidden;
    background: var(--bg);
  }
  .banner__decor {
    position: absolute;
    inset: 0;
    width: 1200px;
    height: 328px;
  }
  .hummingbird-art {
    position: absolute;
    left: 122px;
    top: 56px;
    width: 196px;
    height: 222px;
    border-radius: 46% 54% 40% 60% / 40% 45% 55% 60%;
    background: radial-gradient(ellipse at 45% 40%, rgba(255,255,255,0.55) 0%, rgba(230,220,245,0.35) 45%, rgba(255,255,255,0) 75%);
  }
  .particle-sphere-art {
    position: absolute;
    left: 930px;
    top: 14px;
    width: 262px;
    height: 292px;
    border-radius: 50%;
    background: radial-gradient(circle at 50% 52%, rgba(255,255,255,0.6) 0%, rgba(240,220,250,0.42) 38%, rgba(200,150,230,0.18) 58%, rgba(255,255,255,0) 72%);
  }
  .banner__name {
    position: absolute;
    left: 0;
    width: 1200px;
    top: 92px;
    text-align: center;
    padding-left: 12px;
    font-family: "Mrs Saint Delafield", cursive;
    font-size: 104px;
    line-height: 1;
    font-weight: 400;
    color: var(--white);
    text-shadow: 3px 5px 6px var(--shadow);
    white-space: nowrap;
  }
</style>
</head>
<body>
<main class="banner">
  <svg class="banner__decor" viewBox="0 0 1200 328" aria-hidden="true">
    <!-- grid of faint tiles and pink rules -->
    <g class="grid-lines" stroke="var(--line-pink)" stroke-width="1" fill="none">
      <path d="M60 60 H330 M40 200 H140 M330 265 H460 M820 42 H1010 M1130 42 H1190 V60 M1000 32 V42 M1130 30 V42"/>
      <path d="M20 138 H90 V160 M100 300 H180 M820 240 H960"/>
    </g>
    <g class="grid-tiles" fill="none" stroke="var(--white-faint)" stroke-width="1">
      <rect x="30" y="150" width="20" height="14"/>
      <rect x="54" y="150" width="20" height="14"/>
      <rect x="90" y="150" width="20" height="14"/>
      <rect x="56" y="182" width="16" height="14"/>
      <rect x="56" y="200" width="16" height="14"/>
      <rect x="372" y="72" width="20" height="14"/>
      <rect x="370" y="92" width="110" height="14"/>
      <rect x="480" y="110" width="120" height="12"/>
      <rect x="720" y="104" width="90" height="14"/>
      <rect x="750" y="64" width="16" height="12"/>
      <rect x="1000" y="52" width="18" height="12"/>
      <rect x="1174" y="58" width="16" height="16"/>
      <rect x="1170" y="138" width="16" height="14"/>
      <rect x="1150" y="260" width="14" height="14"/>
    </g>
    <g class="soft-tiles" fill="var(--tint-soft)">
      <rect x="516" y="52" width="14" height="10"/>
      <rect x="520" y="218" width="18" height="12"/>
      <rect x="740" y="218" width="18" height="14"/>
      <rect x="640" y="34" width="22" height="14"/>
      <rect x="300" y="138" width="16" height="12"/>
    </g>

    <!-- central faint mosaic ring -->
    <g class="center-ring" fill="none">
      <circle cx="600" cy="160" r="122" stroke="rgba(255,255,255,0.07)" stroke-width="40"/>
      <circle cx="600" cy="160" r="78" stroke="rgba(255,255,255,0.05)" stroke-width="24"/>
      <circle cx="600" cy="160" r="150" stroke="rgba(255,255,255,0.04)" stroke-width="10" stroke-dasharray="14 8"/>
    </g>

    <!-- HUD rings around the bird -->
    <g class="hud-rings" fill="none">
      <circle cx="248" cy="152" r="132" stroke="rgba(255,255,255,0.09)" stroke-width="2"/>
      <circle cx="248" cy="152" r="118" stroke="rgba(255,255,255,0.12)" stroke-width="6" stroke-dasharray="120 40 60 30"/>
      <circle cx="248" cy="152" r="100" stroke="rgba(255,255,255,0.1)" stroke-width="14" stroke-dasharray="80 60"/>
      <circle cx="248" cy="152" r="150" stroke="rgba(255,255,255,0.07)" stroke-width="3" stroke-dasharray="50 30 200 40"/>
    </g>

    <!-- small ring right -->
    <g class="hud-ring-small" fill="none">
      <circle cx="890" cy="155" r="38" stroke="var(--white-soft)" stroke-width="4"/>
      <circle cx="890" cy="155" r="50" stroke="rgba(255,255,255,0.3)" stroke-width="3" stroke-dasharray="60 18 40 20"/>
    </g>

    <!-- arrow markers -->
    <g class="arrows" fill="rgba(255,255,255,0.6)">
      <path d="M277 140 l8 5 l-8 5z M308 140 l8 5 l-8 5z"/>
      <path d="M256 143 l20 12 l-20 12z" fill="rgba(255,255,255,0.25)"/>
      <path d="M330 143 l20 12 l-20 12z" fill="rgba(255,255,255,0.3)"/>
      <circle cx="252" cy="192" r="2.5"/><circle cx="260" cy="192" r="2.5"/><circle cx="268" cy="192" r="2.5"/><circle cx="276" cy="192" r="2.5"/>
      <path d="M282 187 l8 5 l-8 5z M294 187 l8 5 l-8 5z M306 187 l8 5 l-8 5z"/>
      <path d="M762 60 l20 12 l-20 12z M800 60 l20 12 l-20 12z" fill="rgba(255,255,255,0.3)"/>
      <path d="M796 76 l7 4 l-7 4z M828 76 l7 4 l-7 4z"/>
      <path d="M782 100 l7 4 l-7 4z M794 100 l7 4 l-7 4z M806 100 l7 4 l-7 4z M818 100 l7 4 l-7 4z M830 100 l7 4 l-7 4z M842 100 l7 4 l-7 4z M854 100 l7 4 l-7 4z"/>
      <path d="M846 88 l4 3 l-4 3z M853 88 l4 3 l-4 3z M860 88 l4 3 l-4 3z M867 88 l4 3 l-4 3z M874 88 l4 3 l-4 3z M881 88 l4 3 l-4 3z M888 88 l4 3 l-4 3z" fill="rgba(255,255,255,0.45)"/>
      <path d="M876 97 l4 3 l-4 3z M883 97 l4 3 l-4 3z M890 97 l4 3 l-4 3z M897 97 l4 3 l-4 3z"/>
      <path d="M808 232 l8 5 l-8 5z M838 232 l8 5 l-8 5z"/>
      <path d="M848 246 l6 4 l-6 4z M858 246 l6 4 l-6 4z M868 246 l6 4 l-6 4z M878 246 l6 4 l-6 4z M888 246 l6 4 l-6 4z M904 246 l6 4 l-6 4z M920 246 l6 4 l-6 4z"/>
      <path d="M822 256 l4 3 l-4 3z M830 256 l4 3 l-4 3z M838 256 l4 3 l-4 3z M846 256 l4 3 l-4 3z M856 256 l5 3.5 l-5 3.5z M866 256 l5 3.5 l-5 3.5z M880 264 l5 3.5 l-5 3.5z" fill="rgba(255,255,255,0.45)"/>
      <path d="M822 284 l5 3.5 l-5 3.5z M840 284 l5 3.5 l-5 3.5z"/>
    </g>
  </svg>

  <div class="hummingbird-art" role="img" aria-label="White line-art hummingbird with patterned feathers, hovering with its beak to the right"></div>
  <div class="particle-sphere-art" role="img" aria-label="Glowing sphere made of white and pink particles bursting outward"></div>

  <h1 class="banner__name">LP Thornbury</h1>
</main>
</body>
</html>
```